shopping bags for cosmetics company

We need an illustration that will be fun, young (18 to 28 age range) Our demographic is young makeup artist and enthusiasts. Forward thinking and very artistic. I was thinking along the lines of the attached photos. We do have a logo but I'm not sure how or if we should incorporate it. See the mask photo attached. I am open to other ideas as well...Our color is on our site www.tlvbeauty.com it's an orange color...The illustration should have no more then 4 colors to keep the bag at a reasonable price and this orange should be prominent. I have attached a competitors bag.... Dusk Moth that we really like a lot, we don't want to copy it but want to give you an idea of what our customer is drawn to. So 4 color max... the wording on the bag should be #IamLanternLit The company name is Velvet Lantern Cosmetics www.TLVBeauty.com If you can incorporate our logo found on our site that would be great as well!

Target Market(s)

18 to 25 years old, mostly female. Artists that tend to be edgy and want to carry and edgy bag around the makeup show. It must catch everyones eye and be so different that people will post photos of it on social media. Colorful but only 4 colors or less to keep the price of the bag down. Our target customer is NOT traditional at all

Industry/Entity Type

Cosmetics

Colors
f37123
33a6d7

Requirements
Must have
• Our orange color from our site tlvbeauty.com
#IamLanternLit
Nice to have
• Our gold mask logo would be nice

```html
<!DOCTYPE html>
<html lang="en">
<head>
<meta charset="utf-8">
<title>Velvet Lantern Cosmetics — I am lantern lit</title>
<link rel="stylesheet" href="https://fonts.googleapis.com/css2?family=Outfit:wght@300;400;600&display=swap">
<style>
  :root {
    --backdrop: #e6e7e8;
    --paper: #ffffff;
    --brand-orange: #f37123;
    --deep-orange: #b9581d;
    --pigment-red: #e8452b;
    --pigment-peach: #f6a35c;
    --pigment-blue: #3f6fb0;
    --ink-brown: #7a3a14;
  }
  * { box-sizing: border-box; margin: 0; padding: 0; }
  html, body {
    width: 1200px;
    height: 938px;
    overflow: hidden;
    background: var(--backdrop);
    font-family: "Outfit", "Century Gothic", sans-serif;
  }
  .poster {
    position: absolute;
    left: 293px;
    top: 29px;
    width: 614px;
    height: 880px;
    background: var(--paper);
    overflow: hidden;
  }
  .brand-mark {
    position: absolute;
    top: 30px;
    left: 0;
    width: 100%;
    text-align: center;
    font-weight: 400;
    font-size: 15px;
    letter-spacing: 0.14em;
    color: var(--brand-orange);
  }
  .artwork {
    position: absolute;
    left: 0;
    top: 170px;
    width: 100%;
    height: 710px;
    background:
      radial-gradient(ellipse 34% 30% at 70% 80%, var(--paper) 0 55%, transparent 100%),
      radial-gradient(ellipse 30% 22% at 40% 78%, var(--pigment-blue) 0 40%, transparent 100%),
      linear-gradient(165deg, var(--pigment-peach) 0%, var(--pigment-red) 40%, var(--brand-orange) 65%, var(--pigment-red) 100%);
    -webkit-mask-image: linear-gradient(to bottom, transparent 0%, #000 28%);
            mask-image: linear-gradient(to bottom, transparent 0%, #000 28%);
  }
  .headline {
    position: absolute;
    left: 0;
    top: 92px;
    width: 100%;
    z-index: 2;
    line-height: 0.82;
    background: linear-gradient(to bottom, var(--brand-orange) 0%, var(--brand-orange) 45%, var(--deep-orange) 100%);
    -webkit-background-clip: text;
            background-clip: text;
    color: transparent;
  }
  .headline span { display: block; }
  .headline .line-i-am {
    padding-left: 292px;
    font-weight: 600;
    font-size: 104px;
    letter-spacing: -0.02em;
  }
  .headline .line-lantern {
    padding-left: 160px;
    font-weight: 300;
    font-size: 92px;
    letter-spacing: -0.02em;
  }
  .headline .line-lit {
    padding-left: 136px;
    font-weight: 600;
    font-size: 104px;
    letter-spacing: -0.02em;
  }
  .site-url {
    position: absolute;
    left: 362px;
    top: 743px;
    z-index: 2;
    font-size: 16px;
    font-weight: 400;
    color: var(--ink-brown);
    letter-spacing: 0.01em;
  }
  .site-url b { font-weight: 600; }
</style>
</head>
<body>
  <main class="poster">
    <div class="brand-mark">VELVET LANTERN</div>
    <h1 class="headline">
      <span class="line-i-am">I am</span>
      <span class="line-lantern">lantern</span>
      <span class="line-lit">lit</span>
    </h1>
    <div class="artwork" role="img" aria-label="Painted close-up of a made-up eye with orange and pink shadow, surrounded by crushed orange, red and blue eyeshadow pigments"></div>
    <p class="site-url">www.<b>tlv</b>beauty.com</p>
  </main>
</body>
</html>
```